Carrying bags for customer visit

I am looking to make a carrying case that can be used to carry small presents, gifts, our brochure (20 inch X20 inch) and sometimes our samples (which are printed circuit boards that have a size of 24X15). The case should look elegant, show our company logo and our slogan "BOARDS ARE OUR CRAFT". You can try to download our logo from our web site www.tarnvolt.com. I want a contemporary and cool feel of the carrying case that can be any materials. I prefer to use recyclable materials that reflects our company's business philosophy of practicing sustanbility. Also I would like to add Chinese name “锦泰电路(东莞)有限公司" in the bag.
Updates

Need extra days to review

Target Market(s)

Corporate customers who will come into contact with our companies

Colors

Designer to choose colors to be used in the design.

Requirements
Must have
• It has to be attractive and people wanting to use them on a regular basis. Therefore, the logo display and our slogan should be subtle. I want the carrying bags not to be very expensive to produce.

```html
<!DOCTYPE html>
<html lang="en">
<head>
<meta charset="utf-8">
<title>Tarnvolt Carrying Bag – Front Face</title>
<link href="https://fonts.googleapis.com/css2?family=Cinzel:wght@400;700&family=Noto+Sans+SC:wght@400&display=swap" rel="stylesheet">
<style>
  :root {
    --backdrop: #e6e6e6;
    --paper: #f7f7f7;
    --pcb-green: #014723;
    --ink-black: #050505;
    --slate: #5b5b5b;
    --gold: #b8950f;
    --hairline: #3a3a3a;
    --ornament: #c4c4c4;
  }
  html, body {
    margin: 0;
    width: 1200px;
    height: 1200px;
    overflow: hidden;
    background: var(--backdrop);
  }
  .bag-face {
    position: absolute;
    left: 255px;
    top: 90px;
    width: 690px;
    height: 1020px;
    background: var(--paper);
    overflow: hidden;
    box-shadow: 0 2px 10px rgba(0,0,0,0.08);
  }
  .frame-line {
    position: absolute;
    top: 40px;
    width: 1px;
    height: 560px;
    background: var(--hairline);
  }
  .frame-line.left { left: 34px; }
  .frame-line.right { right: 34px; }
  .frame-top {
    position: absolute;
    top: 40px;
    height: 1px;
    width: 150px;
    background: var(--hairline);
  }
  .frame-top.left { left: 34px; }
  .frame-top.right { right: 34px; }
  .corner-ornament {
    position: absolute;
    top: 40px;
    width: 66px;
    height: 66px;
    background: linear-gradient(135deg, var(--ornament), #e4e4e4);
  }
  .corner-ornament.left { left: 34px; }
  .corner-ornament.right { right: 34px; }
  .brand {
    position: absolute;
    top: 420px;
    left: 0;
    right: 0;
    text-align: center;
  }
  .brand-name {
    font-family: "Cinzel", serif;
    font-weight: 700;
    font-size: 78px;
    letter-spacing: 4px;
    color: var(--pcb-green);
    line-height: 1;
  }
  .slogan {
    margin-top: 18px;
    font-family: "Cinzel", serif;
    font-weight: 400;
    font-size: 38px;
    letter-spacing: 1px;
    color: var(--gold);
    line-height: 1;
  }
  .wave-bands {
    position: absolute;
    left: 0;
    top: 0;
    width: 690px;
    height: 1020px;
  }
  .company-label {
    position: absolute;
    left: 50%;
    transform: translateX(-50%);
    bottom: 48px;
    background: var(--pcb-green);
    color: #ffffff;
    font-family: "Noto Sans SC", sans-serif;
    font-size: 25px;
    padding: 8px 26px;
    white-space: nowrap;
    letter-spacing: 1px;
  }
</style>
</head>
<body>
  <main class="bag-face">
    <div class="frame-top left"></div>
    <div class="frame-top right"></div>
    <div class="frame-line left"></div>
    <div class="frame-line right"></div>
    <div class="corner-ornament left" role="img" aria-label="Decorative filigree corner ornament"></div>
    <div class="corner-ornament right" role="img" aria-label="Decorative filigree corner ornament"></div>

    <div class="brand">
      <div class="brand-name">TARNVOLT</div>
      <div class="slogan">BOARDS ARE OUR CRAFT</div>
    </div>

    <svg class="wave-bands" viewBox="0 0 690 1020" aria-hidden="true">
      <path d="M0 610 Q170 700 350 765 L0 765 Z" fill="var(--pcb-green)"/>
      <path d="M690 630 Q500 700 350 765 L690 765 Z" fill="var(--ink-black)"/>
      <path d="M0 765 L690 765 L690 800 Q520 780 350 770 Q170 780 0 800 Z" fill="var(--paper)"/>
      <path d="M0 812 Q170 792 350 782 Q520 792 690 812 L690 1020 L0 1020 Z" fill="var(--slate)"/>
    </svg>

    <div class="company-label">锦泰电路（东莞）有限公司</div>
  </main>
</body>
</html>
```